Cover for Where the Quiet River Bends Beyond Our Morning

Cover for a book that describes everything that happens to a person, from pre-birth life plans through growing in compassion and wisdom to death and living in the afterlife. The information is revealed in messages from people living in the life after this life. The title is Lanterns Along the Hidden Stair of Every Soul: Gathered from Voices Dwelling in the Further Meadow. Author is T. Morven Ashdale. Book size is 6 by 9.

Target Market(s)

General

Font styles to use
Serif

```html
<!DOCTYPE html>
<html lang="en">
<head>
<meta charset="utf-8">
<title>Lanterns Along the Hidden Stair of Every Soul — Book Cover</title>
<link rel="stylesheet" href="https://fonts.googleapis.com/css2?family=Cinzel:wght@400;500&family=Cormorant+SC:wght@500&display=swap">
<style>
  :root {
    --page-bg: #ffffff;
    --ink-white: #ffffff;
    --ink-shadow: #1a1f5c;
    --author-band: #27306e;
    --rule-light: #c9d3f2;
    --sky-top: #434c9e;
    --sky-mid: #4b62b4;
    --horizon: #7fa6d6;
    --ground: #4c69b8;
    --ground-low: #5a74bc;
  }
  html, body {
    margin: 0;
    width: 1200px;
    height: 1200px;
    overflow: hidden;
    background: var(--page-bg);
  }
  .book-cover {
    position: absolute;
    left: 233px;
    top: 50px;
    width: 733px;
    height: 1100px;
    display: block;
  }
  .cover-art-fill { fill: url(#coverArtGradient); }
  .author-band { fill: var(--author-band); }
  .author-name {
    font-family: "Cormorant SC", "Cinzel", serif;
    font-weight: 500;
    font-size: 34px;
    letter-spacing: 1px;
    fill: var(--ink-white);
  }
  .title-block {
    filter: drop-shadow(3px 3px 0 var(--ink-shadow));
  }
  .title-line {
    font-family: "Cinzel", serif;
    font-weight: 500;
    font-size: 66px;
    fill: var(--ink-white);
  }
  .title-rule, .subtitle-rule {
    stroke: var(--rule-light);
    stroke-width: 4;
    opacity: 0.75;
  }
  .subtitle-line {
    font-family: "Cinzel", serif;
    font-size: 38px;
    fill: var(--ink-white);
    letter-spacing: 1px;
  }
</style>
</head>
<body>
<svg class="book-cover" viewBox="0 0 830 1245" xmlns="http://www.w3.org/2000/svg">
  <defs>
    <linearGradient id="coverArtGradient" x1="0" y1="0" x2="0" y2="1">
      <stop offset="0" stop-color="var(--sky-top)"/>
      <stop offset="0.45" stop-color="var(--sky-mid)"/>
      <stop offset="0.6" stop-color="var(--horizon)"/>
      <stop offset="0.72" stop-color="var(--ground)"/>
      <stop offset="1" stop-color="var(--ground-low)"/>
    </linearGradient>
  </defs>

  <rect class="cover-art-fill" x="0" y="0" width="830" height="1245" role="img"
        aria-label="Textured blue collage of faint overlapping words above a misty horizon, with a lone figure walking along a glowing tiled path"/>

  <g class="author">
    <rect class="author-band" x="242" y="0" width="341" height="103"/>
    <text class="author-name" x="412" y="80" text-anchor="middle">T. MORVEN ASHDALE</text>
  </g>

  <g class="title-block">
    <text class="title-line" x="415" y="288" text-anchor="middle" textLength="650" lengthAdjust="spacing">LANTERNS</text>
    <line class="title-rule" x1="95" y1="300" x2="745" y2="300"/>
    <text class="title-line" x="415" y="370" text-anchor="middle" textLength="600" lengthAdjust="spacing">ALONG THE</text>
    <line class="title-rule" x1="95" y1="384" x2="735" y2="384"/>
    <text class="title-line" x="415" y="450" text-anchor="middle">HIDDEN STAIR</text>
    <line class="title-rule" x1="95" y1="466" x2="745" y2="466"/>
    <text class="title-line" x="415" y="533" text-anchor="middle">OF EVERY</text>
    <line class="title-rule" x1="180" y1="549" x2="748" y2="549"/>
    <text class="title-line" x="415" y="613" text-anchor="middle">SOUL</text>
  </g>

  <g class="subtitle">
    <line class="subtitle-rule" x1="0" y1="1013" x2="830" y2="1013"/>
    <text class="subtitle-line" x="415" y="1060" text-anchor="middle">GATHERED FROM VOICES</text>
    <text class="subtitle-line" x="415" y="1110" text-anchor="middle">DWELLING IN THE FURTHER MEADOW</text>
    <line class="subtitle-rule" x1="0" y1="1138" x2="830" y2="1138"/>
  </g>
</svg>
</body>
</html>
```